Multi-Line Insurance PPC Landing Page - Conversion optimized.

We have a PPC landing page used for the general population to get an insurance quote through an agent's site.

We'd like to improve the page for PPC traffic, make it more conversion friendly.

Site should be a single long page.

We will dynamically change the form and headlines on the page depending on what insurance "line" is being called. ie, Lift, Auto, Home, Business.

The enclosed AI file has all of the raw elements we need. We're looking to enhance the design and conversion ability.

Target Market(s)

General public needed insurance services.

Industry/Entity Type

Insurance Broker

Number of Pages Required

1 page

Font styles to use
Sans Serif

Requirements
Must have
• Form, agent picture, name, address.

```html
<!DOCTYPE html>
<html lang="en">
<head>
<meta charset="utf-8">
<title>Harborline Insurance – Get a Quote</title>
<link href="https://fonts.googleapis.com/css2?family=Open+Sans:wght@400;600;700&family=Noto+Serif:wght@400;700&display=swap" rel="stylesheet">
<style>
:root{
  --green:#5aad2f;
  --green-dark:#3f8a1c;
  --green-light:#7cc24f;
  --blue:#1f5f9e;
  --text:#333a40;
  --muted:#666d73;
  --line:#cfd6cc;
  --field:#f4f6f3;
  --white:#ffffff;
  --footer:#4b9a25;
}
*{box-sizing:border-box;margin:0;padding:0}
html,body{width:1200px;height:2216px;overflow:hidden;background:var(--white)}
body{font-family:"Open Sans",Arial,sans-serif;color:var(--text);position:relative}

.hero{position:absolute;left:0;top:0;width:1200px;height:400px;
  background:linear-gradient(100deg,#b9d7a6 0%,#e8efe2 35%,#c9c0b0 60%,#9fc48a 100%)}
.call-box{position:absolute;right:20px;top:14px;width:250px;height:62px;background:var(--white);
  border-radius:4px;box-shadow:0 2px 6px rgba(0,0,0,.2);padding:8px 14px}
.call-box .label{font-size:12px;color:var(--muted)}
.call-box .phone{display:flex;align-items:center;gap:8px;font-size:22px;font-weight:700;color:var(--text);margin-top:2px}
.call-box svg{width:20px;height:20px;fill:var(--green)}

.quote-band{position:absolute;left:0;top:400px;width:1200px;height:420px;
  background:linear-gradient(180deg,var(--green-light),var(--green))}
.agent{position:absolute;left:60px;top:0;width:330px;height:420px;color:var(--white)}
.agent-photo{position:absolute;left:10px;top:14px;width:190px;height:210px;
  background:linear-gradient(180deg,#dfe7ea,#8b969c);border-radius:2px}
.agent-brand{position:absolute;left:10px;top:240px;display:flex;align-items:center;gap:10px;
  font-size:30px;font-weight:700;color:var(--white);line-height:1.2}
.agent-brand .mark{width:22px;height:22px;border-radius:50%;background:var(--white)}
.agent-name{position:absolute;left:10px;top:292px;font-size:20px;font-weight:600}
.agent-addr{position:absolute;left:10px;top:324px;font-size:13px}
.agent-phone{position:absolute;left:10px;top:354px;display:flex;align-items:center;gap:8px;font-size:22px;font-weight:700}
.agent-phone svg{width:20px;height:20px;fill:var(--white)}

.quote-panel{position:absolute;left:450px;top:0;width:720px;height:420px;background:var(--white);
  padding:30px 40px 0}
.quote-panel h1{text-align:center;font-family:"Noto Serif",Georgia,serif;font-weight:400;font-size:24px;color:var(--text);line-height:1.35}
.quote-form{display:grid;grid-template-columns:1fr 1fr;gap:14px 20px;margin:26px 0 0 90px;width:540px}
.field{height:40px;border:1px solid var(--line);background:var(--field);font-size:13px;color:var(--muted);
  padding:0 12px;display:flex;align-items:center;justify-content:space-between}
.field.select::after{content:"";border:5px solid transparent;border-top-color:var(--muted);margin-top:5px}
.date-row{display:grid;grid-template-columns:1fr 1fr 1fr;gap:8px}
.submit{grid-column:2;height:44px;background:var(--green);color:var(--white);font-size:17px;font-weight:600;
  display:flex;align-items:center;justify-content:center;border-radius:3px}

.intro{position:absolute;left:0;top:845px;width:1200px;text-align:center;font-family:"Noto Serif",Georgia,serif}
.intro .lead{font-size:18px;color:var(--text);line-height:1.45}
.intro .sub{font-size:18px;color:var(--blue);margin-top:8px;line-height:1.45}
.intro .cta{font-size:18px;color:var(--green-dark);font-weight:700;line-height:1.45}

.lines{position:absolute;left:60px;top:1000px;width:1080px;display:grid;grid-template-columns:repeat(3,1fr);gap:40px 30px}
.line-card{border:1px solid var(--line);height:400px;background:var(--white);position:relative}
.line-card h2{height:40px;background:var(--green);color:var(--white);font-size:17px;font-weight:600;
  padding:0 14px;display:flex;align-items:center}
.line-card .photo{height:150px;margin:0}
.line-card p{font-size:12.5px;line-height:1.55;color:var(--muted);padding:14px 16px 0}
.line-card .btn{position:absolute;left:16px;bottom:16px;border:1px solid var(--line);background:var(--field);
  font-size:13px;padding:7px 14px;color:var(--text)}
.ph-auto{background:linear-gradient(135deg,#a9b7c4,#d8dde1)}
.ph-home{background:linear-gradient(135deg,#c7a58a,#e7ddd2)}
.ph-life{background:linear-gradient(135deg,#8fb3cc,#d9c2a8)}
.ph-health{background:linear-gradient(135deg,#6f8fa8,#d5dde3)}
.ph-business{background:linear-gradient(135deg,#4f6f8f,#b6c6d4)}
.ph-disability{background:linear-gradient(135deg,#b8c9a0,#e3d8c5)}

.footer{position:absolute;left:0;top:2096px;width:1200px;height:120px;background:var(--footer);color:var(--white);
  text-align:center;font-size:13px;padding-top:18px;line-height:1.9}
.footer nav{display:flex;justify-content:center;gap:22px;font-weight:600}
</style>
</head>
<body>

<header class="hero" role="img" aria-label="Photo of a smiling family outdoors">
  <div class="call-box">
    <div class="label">Get a quick quote by phone</div>
    <div class="phone"><svg viewBox="0 0 24 24"><path d="M6.6 10.8a15.1 15.1 0 0 0 6.6 6.6l2.2-2.2a1 1 0 0 1 1-.25 11.4 11.4 0 0 0 3.6.57 1 1 0 0 1 1 1V20a1 1 0 0 1-1 1A17 17 0 0 1 3 4a1 1 0 0 1 1-1h3.5a1 1 0 0 1 1 1c0 1.25.2 2.45.57 3.57a1 1 0 0 1-.25 1z"/></svg>555-014-2290</div>
  </div>
</header>

<section class="quote-band">
  <div class="agent">
    <div class="agent-photo" role="img" aria-label="Portrait of the agent in a suit"></div>
    <div class="agent-brand"><span class="mark"></span>Harborline</div>
    <div class="agent-name">Marcus Hale - Agent</div>
    <div class="agent-addr">1480 Cedar Ave Riverton, CA 90321</div>
    <div class="agent-phone"><svg viewBox="0 0 24 24"><path d="M6.6 10.8a15.1 15.1 0 0 0 6.6 6.6l2.2-2.2a1 1 0 0 1 1-.25 11.4 11.4 0 0 0 3.6.57 1 1 0 0 1 1 1V20a1 1 0 0 1-1 1A17 17 0 0 1 3 4a1 1 0 0 1 1-1h3.5a1 1 0 0 1 1 1c0 1.25.2 2.45.57 3.57a1 1 0 0 1-.25 1z"/></svg>555-014-2290</div>
  </div>

  <div class="quote-panel">
    <h1>Get an instant life insurance quote.<br>A fast and secure way to get a quote quickly.</h1>
    <div class="quote-form">
      <div class="field">Full Name</div>
      <div class="field select">Height / Weight</div>
      <div class="field select">Select Sex</div>
      <div class="field select">Select Tobacco Use</div>
      <div class="date-row">
        <div class="field select">Month</div>
        <div class="field select">Day</div>
        <div class="field select">Year</div>
      </div>
      <div class="field">Mobile Number</div>
      <div class="field select">Select Current Health</div>
      <div class="field">Email Address</div>
      <div class="submit">Show The Quote</div>
    </div>
  </div>
</section>

<section class="intro">
  <p class="lead">We cover all your insurance needs at the best prices, guaranteed.</p>
  <p class="sub">Tailoring insurance coverage around your needs is easier than you think. We're here to help<br>you learn more about all your options and provide answers to common questions.</p>
  <p class="cta">Ready to take the next step?</p>
</section>

<section class="lines">
  <article class="line-card">
    <h2>Auto Insurance</h2>
    <div class="photo ph-auto" role="img" aria-label="Photo of a driver at the wheel"></div>
    <p>Get the protection you need at a price you can afford. Our agents compare coverage options for you and help you find the right policy for your car, your budget and your daily drive.</p>
    <span class="btn">Get A Quote</span>
  </article>
  <article class="line-card">
    <h2>Home Insurance</h2>
    <div class="photo ph-home" role="img" aria-label="Photo of hands sheltering a model house"></div>
    <p>Whether you own or rent, your home is one of your biggest investments. We help protect your house, your belongings and your family with coverage built around the way you live.</p>
    <span class="btn">Get A Quote</span>
  </article>
  <article class="line-card">
    <h2>Life Insurance</h2>
    <div class="photo ph-life" role="img" aria-label="Photo of a happy family together"></div>
    <p>We can help you find coverage that is right for you and your loved ones, from simple term plans to permanent policies. Our planning tools make it easy to choose with confidence.</p>
    <span class="btn">Get A Quote</span>
  </article>
  <article class="line-card">
    <h2>Health Insurance</h2>
    <div class="photo ph-health" role="img" aria-label="Photo of a doctor with a patient"></div>
    <p>As life changes, your health coverage should keep pace. We review your needs and explain your options so you can pick a plan that protects you and your family without surprises.</p>
    <span class="btn">Get A Quote</span>
  </article>
  <article class="line-card">
    <h2>Business Insurance</h2>
    <div class="photo ph-business" role="img" aria-label="Photo of a business handshake"></div>
    <p>We know your business means everything to you. Our agents help you find coverage for property, liability and staff so you can focus on growth and handle challenges with ease.</p>
    <span class="btn">Get A Quote</span>
  </article>
  <article class="line-card">
    <h2>Disability Insurance</h2>
    <div class="photo ph-disability" role="img" aria-label="Photo of a person in a wheelchair outdoors"></div>
    <p>These plans are designed to help keep you financially stable during difficult times. If illness or injury keeps you from working, disability coverage can replace part of your income.</p>
    <span class="btn">Get A Quote</span>
  </article>
</section>

<footer class="footer">
  <div>This landing page built for: Marcus Hale - Agent · 1480 Cedar Ave Riverton, CA 90321 · 555-014-2290</div>
  <nav><span>Auto Insurance</span><span>Home Insurance</span><span>Life Insurance</span><span>Health Insurance</span><span>Business Insurance</span><span>Disability Insurance</span></nav>
  <div>© 2015 Coverwell Agents. All Rights Reserved · Privacy Policy · Terms &amp; Conditions</div>
</footer>

</body>
</html>
```